Kneadwell Bodycare

We are a Massage Therapy business based in Invercargill, New Zealand. We specialise in Sports and deep tissue massage but also provide relaxation and aromatherapy massage. We would like to see designs that use the the logo.
The final design should promote health and fitness.
Updates

Hi I am getting feedback that my business card picture is poor quality. I got this picture from plaza press under massage. So if you google this image a better quality picture should come up,. If not hope to upload a better image by tomorow, thanks.

Target Market(s)

Sports, people with pain and injuries

Industry/Entity Type

Massage

Requirements
Must have
• Logo, muscle body that is used on the business card, also a poster that matches my business card
Nice to have
• Picture of muscle man, shown on my business card
Should not have
• Not a picture of a real person

```html
<!DOCTYPE html>
<html lang="en">
<head>
<meta charset="utf-8">
<title>Kneadwell Bodycare – Are You In Pain?</title>
<link href="https://fonts.googleapis.com/css2?family=Antonio:wght@700&family=Oswald:wght@400;500&family=Kaushan+Script&display=swap" rel="stylesheet">
<style>
  :root {
    --navy: #28306f;
    --sky: #5f97d3;
    --paper: #ffffff;
  }
  html, body {
    margin: 0;
    padding: 0;
    overflow: hidden;
    background: var(--paper);
  }
  .poster {
    position: relative;
    width: 850px;
    height: 1200px;
    overflow: hidden;
    background: var(--paper);
    box-sizing: border-box;
    border: 2px solid var(--navy);
    font-family: "Oswald", sans-serif;
    color: var(--navy);
  }
  .anatomy-art {
    position: absolute;
    left: 0;
    top: 0;
    width: 265px;
    height: 354px;
    background: linear-gradient(135deg, #d9d9d9 0%, #9c9c9c 45%, #6d6d6d 75%, #bdbdbd 100%);
  }
  .headline {
    position: absolute;
    margin: 0;
    font-family: "Antonio", sans-serif;
    font-weight: 700;
    line-height: 1;
    text-transform: uppercase;
    transform-origin: left top;
    white-space: nowrap;
  }
  .headline-top {
    left: 278px;
    top: 36px;
    font-size: 132px;
    color: var(--navy);
    transform: scaleX(0.8);
  }
  .headline-bottom {
    left: 434px;
    top: 160px;
    font-size: 170px;
    color: var(--sky);
    letter-spacing: 2px;
    transform: scaleX(0.86);
  }
  .brand-band {
    position: absolute;
    left: 0;
    top: 358px;
    width: 100%;
    height: 200px;
    background: var(--navy);
  }
  .brand-mark {
    position: absolute;
    left: 45px;
    top: 6px;
    width: 174px;
    height: 174px;
    box-sizing: border-box;
    border-radius: 50%;
    border: 8px solid var(--paper);
  }
  .brand-name {
    position: absolute;
    left: 250px;
    top: 70px;
    width: 480px;
    text-align: center;
    margin: 0;
    font-family: "Oswald", sans-serif;
    font-weight: 400;
    font-size: 46px;
    line-height: 1.2;
    color: var(--paper);
    white-space: nowrap;
  }
  .services {
    position: absolute;
    left: 40px;
    top: 612px;
    width: 390px;
    margin: 0;
    padding: 0;
    list-style: none;
    text-align: center;
    font-size: 45px;
    font-weight: 500;
    line-height: 68px;
  }
  .booking {
    position: absolute;
    left: 452px;
    top: 582px;
    width: 370px;
  }
  .booking-stroke {
    position: absolute;
    left: 2px;
    top: 50px;
    width: 228px;
    height: 24px;
    background: var(--sky);
    border-radius: 40% 8% 60% 10%;
    transform: rotate(-3deg);
  }
  .booking-cta {
    position: relative;
    margin: 0;
    font-family: "Kaushan Script", cursive;
    font-size: 44px;
    line-height: 1;
    color: var(--navy);
    transform: rotate(-6deg);
    transform-origin: left center;
  }
  .booking-phone {
    position: absolute;
    left: 136px;
    top: 66px;
    margin: 0;
    font-size: 33px;
    font-weight: 500;
    white-space: nowrap;
  }
  .prices {
    position: absolute;
    left: 516px;
    top: 742px;
    margin: 0;
  }
  .prices-title {
    margin: 0 0 4px;
    font-size: 34px;
    font-weight: 400;
    color: var(--sky);
    line-height: 1.2;
  }
  .prices-list {
    margin: 0;
    padding: 0;
    list-style: none;
    font-size: 34px;
    font-weight: 500;
    line-height: 49px;
  }
  .footer {
    position: absolute;
    left: 0;
    top: 1022px;
    width: 100%;
    text-align: center;
  }
  .therapist {
    margin: 0;
    font-size: 28px;
    font-weight: 400;
    letter-spacing: 0.5px;
    text-transform: uppercase;
  }
  .contact {
    margin: 14px 0 0;
    font-size: 22px;
    color: var(--sky);
  }
  .contact .divider {
    margin: 0 24px;
  }
  .social {
    margin: 14px 0 0;
    font-size: 22px;
    font-weight: 500;
    color: var(--navy);
    display: flex;
    justify-content: center;
    align-items: center;
    gap: 8px;
  }
  .social-square {
    display: inline-block;
    width: 26px;
    height: 26px;
    background: var(--navy);
  }
</style>
</head>
<body>
<main class="poster">
  <div class="anatomy-art" role="img" aria-label="Grey anatomical illustration of a muscular shoulder and arm with highlighted pain points"></div>

  <h1 class="headline headline-top">Are you in</h1>
  <p class="headline headline-bottom">Pain?</p>

  <header class="brand-band">
    <span class="brand-mark" aria-hidden="true"></span>
    <p class="brand-name">Kneadwell Bodycare</p>
  </header>

  <ul class="services">
    <li>Deep Tissue</li>
    <li>Sports Massage</li>
    <li>Remedial Massage</li>
    <li>Relaxation</li>
    <li>Aromatherapy</li>
  </ul>

  <section class="booking">
    <div class="booking-stroke" role="img" aria-label="Blue brush stroke"></div>
    <p class="booking-cta">Book today!</p>
    <p class="booking-phone">Call 0275550142</p>
  </section>

  <section class="prices">
    <h2 class="prices-title">PRICES</h2>
    <ul class="prices-list">
      <li>30 minutes: $40</li>
      <li>60 minutes: $60</li>
      <li>90 minutes: $80</li>
    </ul>
  </section>

  <footer class="footer">
    <p class="therapist">Maren Holt, Bachelor of Therapeutic &amp; Sports Massage</p>
    <p class="contact">15 Rowan St, Invercargill<span class="divider">|</span>www.kneadwell.co.nz</p>
    <p class="social">Like us on Linkwall! <span class="social-square" aria-hidden="true"></span></p>
  </footer>
</main>
</body>
</html>
```